Makeupbyfernandflick banner

Hi I am a makeup artist looking at getting my banner created, I will be sending a picture below as a example of what I want, it's what an other makeup artist has done on her banner and I love it !
I will be also sending the pictures that you will need to put it together and will also attach a picture of what I would want written in the middle, please try and match the writing showen in the example.
Please feel free to ask any questions
Thank you
Marlene Tobrecht

```html
<!DOCTYPE html>
<html lang="en">
<head>
<meta charset="utf-8">
<title>Makeupbyfernandflick banner</title>
<link rel="stylesheet" href="https://fonts.googleapis.com/css2?family=Raleway:wght@400;500;700;800&display=swap">
<style>
  :root {
    --red: #b8141c;
    --ink: #111111;
    --paper: #ffffff;
    --blush: #faf3f4;
  }
  * { margin: 0; padding: 0; box-sizing: border-box; }
  html, body { width: 1200px; height: 2743px; overflow: hidden; }
  body {
    font-family: "Raleway", "Century Gothic", sans-serif;
    color: var(--ink);
    background: linear-gradient(180deg, var(--paper) 0%, var(--blush) 45%, var(--paper) 100%);
    position: relative;
  }
  .banner { position: absolute; inset: 0; }

  .lips-art {
    position: absolute; left: 40px; top: 0; width: 1120px; height: 730px;
    border-radius: 50% / 46%;
    background: radial-gradient(ellipse at 50% 50%, #f7c9cc 0%, #e0343f 38%, #c8121d 62%, rgba(200,18,29,0) 72%);
  }
  .brand-name {
    position: absolute; left: 0; right: 0; top: 358px;
    text-align: center; font-size: 74px; line-height: 96px; font-weight: 700; color: var(--ink);
  }

  .artist-name {
    position: absolute; left: 0; right: 0; top: 750px;
    text-align: center; font-size: 104px; line-height: 120px; font-weight: 800; color: var(--red);
  }
  .artist-role {
    position: absolute; left: 0; right: 0; top: 892px;
    text-align: center; font-size: 86px; line-height: 108px; font-weight: 400;
  }
  .artist-tagline {
    position: absolute; left: 0; right: 0; top: 1025px;
    text-align: center; font-size: 55px; line-height: 74px; font-weight: 500;
  }

  .bio {
    position: absolute; left: 40px; right: 40px; top: 1165px;
    text-align: center; font-size: 40px; line-height: 61px; font-weight: 500;
    white-space: nowrap;
  }
  .bio strong { color: var(--red); font-weight: 800; }

  .contact-phone {
    position: absolute; left: 0; right: 0; top: 1832px;
    text-align: center; font-size: 68px; line-height: 84px; font-weight: 400; color: var(--red);
  }
  .contact-email {
    position: absolute; left: 0; right: 0; top: 1925px;
    text-align: center; font-size: 54px; line-height: 70px; font-weight: 400; color: var(--red);
  }

  .social-row {
    position: absolute; left: 0; right: 0; top: 2075px; height: 110px;
    display: flex; justify-content: center; gap: 130px; align-items: center;
  }
  .social-item { display: flex; align-items: center; gap: 24px; }
  .social-dot { width: 64px; height: 64px; background: var(--red); border-radius: 50%; }
  .social-name { font-size: 58px; font-weight: 700; line-height: 1; color: var(--ink); }

  .kit-art {
    position: absolute; left: 40px; top: 2280px; width: 640px; height: 440px;
    border-radius: 40px;
    background: radial-gradient(ellipse at 50% 55%, #e6c9a0 0%, #d88a9a 45%, rgba(255,255,255,0) 75%);
  }
  .brush-art {
    position: absolute; left: 700px; top: 2290px; width: 460px; height: 420px;
    border-radius: 40px;
    background: radial-gradient(ellipse at 40% 40%, #f0d6c4 0%, #d9b184 45%, rgba(255,255,255,0) 75%);
  }
</style>
</head>
<body>
<main class="banner">
  <div class="lips-art" role="img" aria-label="Red lipstick kiss print"></div>
  <div class="brand-name">makeupby FernandFlick</div>

  <h1 class="artist-name">Marlene Tobrecht</h1>
  <p class="artist-role">Makeup Artist</p>
  <p class="artist-tagline">Specialising in all things makeup</p>

  <p class="bio">Marlene is a qualified makeup artist based in<br>Sydney, her <strong>experience within the<br>makeup industry of over 5 years.</strong><br>Marlene's impeccable makeup shows through<br>her work and her clientele old and new<br>becoming not just clients but friends her<br>personality is not only bubbly and friendly but<br>also warm and very caring she pays a lot of her<br>attention to details and will perfect each look as<br>the client requests.</p>

  <p class="contact-phone">0412586304</p>
  <p class="contact-email">Makeupbyfernandflick@mailpost.com</p>

  <div class="social-row">
    <div class="social-item">
      <span class="social-dot"></span>
      <span class="social-name">Glowline</span>
    </div>
    <div class="social-item">
      <span class="social-dot"></span>
      <span class="social-name">Shutterlane</span>
    </div>
  </div>

  <div class="kit-art" role="img" aria-label="Open makeup case with lipsticks, brushes and palettes"></div>
  <div class="brush-art" role="img" aria-label="Powder brush with loose face powder"></div>
</main>
</body>
</html>
```